Design a Professional Business Card for Vello Marra

Design a business card for Vello Marra, we are a National Sport Court Company.

West Region Address: 4172 Glen Harrow Ct, Suite #210 Englewood, Colorado 80112
East Region Address: 7316 38th Ave W, Bradenton, Florida 34210

Target Market(s)

High End Residential & Institutional Clients

Industry/Entity Type

Design & Construction

Contact Information for Business Card

Logo/Brand/Colors/ name, number (provided in comments)

Requirements
Must have
• Colors only provided in logo
Should not have
• Any other colors not in existing logo (attached)

```html
<!DOCTYPE html>
<html lang="en">
<head>
<meta charset="utf-8">
<title>Vello Marra – Business Card</title>
<link rel="stylesheet" href="https://fonts.googleapis.com/css2?family=Poppins:wght@400;500;600;700&display=swap">
<style>
  :root {
    --navy: #1f3468;
    --green: #056633;
    --white: #ffffff;
    --paper: #f4f5f6;
    --ink: #1b1b1b;
    --stage: #d9dbde;
  }
  * { box-sizing: border-box; margin: 0; padding: 0; }
  html, body { width: 1200px; height: 900px; overflow: hidden; }
  body {
    background: var(--stage);
    font-family: "Poppins", sans-serif;
    position: relative;
  }
  .card {
    position: absolute;
    left: 290px;
    width: 620px;
    height: 354px;
    border-radius: 22px;
    overflow: hidden;
  }
  /* Back side */
  .card--back { top: 70px; background: var(--green); }
  .back-band {
    position: absolute; left: 0; top: 0; width: 100%; height: 96px;
    background: var(--navy);
  }
  .back-stripe {
    position: absolute; left: 0; bottom: 44px; width: 100%; height: 22px;
    background: var(--white);
  }
  .back-name {
    position: absolute; right: 44px; bottom: 92px;
    color: var(--white); font-weight: 700; font-size: 34px;
    letter-spacing: 3px; text-transform: uppercase; line-height: 1.05;
    text-align: left;
  }
  /* Front side */
  .card--front { top: 476px; background: var(--paper); color: var(--ink); }
  .brand {
    position: absolute; left: 140px; top: 38px;
    display: flex; align-items: center; gap: 22px;
  }
  .brand-dot { width: 78px; height: 78px; border-radius: 50%; background: var(--navy); flex: none; }
  .brand-name {
    color: var(--navy); font-weight: 700; font-size: 42px;
    letter-spacing: 4px; text-transform: uppercase; line-height: 1; white-space: nowrap;
  }
  .rule { position: absolute; height: 2px; background: var(--navy); }
  .rule--top { left: 40px; top: 146px; width: 300px; }
  .rule--bottom { right: 40px; top: 238px; width: 290px; }
  .person { position: absolute; left: 240px; top: 156px; width: 350px; text-align: center; }
  .person-name { color: var(--navy); font-weight: 700; font-size: 22px; line-height: 1.2; white-space: nowrap; }
  .person-title { font-size: 12px; line-height: 1.3; color: #333; }
  .contacts { position: absolute; left: 40px; top: 184px; list-style: none; }
  .contacts li {
    display: flex; align-items: center; gap: 9px;
    font-size: 13.5px; line-height: 23px; white-space: nowrap;
  }
  .contacts svg { width: 12px; height: 12px; fill: var(--green); flex: none; }
  .regions { position: absolute; right: 40px; top: 250px; width: 290px; font-size: 12.5px; line-height: 1.4; }
  .region + .region { margin-top: 6px; }
  .region-label { color: var(--green); font-weight: 600; }
</style>
</head>
<body>
  <section class="card card--back" aria-label="Card back">
    <div class="back-band"></div>
    <div class="back-stripe"></div>
    <div class="back-name">Vello<br>Marra</div>
  </section>

  <section class="card card--front" aria-label="Card front">
    <div class="brand">
      <span class="brand-dot"></span>
      <span class="brand-name">Vello Marra</span>
    </div>
    <div class="rule rule--top"></div>
    <div class="person">
      <p class="person-name">Daniel R. Whitford, ASLA</p>
      <p class="person-title">CEO &amp; Founder</p>
    </div>
    <ul class="contacts">
      <li><svg viewBox="0 0 12 12"><path d="M2.5 1l2 2.2-1 1.3a6 6 0 0 0 4 4l1.3-1 2.2 2-1.3 1.5C5.5 11 1 6.5 1 2.3z"/></svg>1-800-555-0142</li>
      <li><svg viewBox="0 0 12 12"><path d="M3 0h6a1 1 0 0 1 1 1v10a1 1 0 0 1-1 1H3a1 1 0 0 1-1-1V1a1 1 0 0 1 1-1zm0 1.5v8h6v-8z"/></svg>(303) 555-0173</li>
      <li><svg viewBox="0 0 12 12"><path d="M0 2h12v8H0zM.8 2.6L6 6.6l5.2-4z" fill-rule="evenodd"/></svg>daniel@vellomarra.com</li>
      <li><svg viewBox="0 0 12 12"><circle cx="6" cy="6" r="5.5"/></svg>www.vellomarra.com</li>
    </ul>
    <div class="rule rule--bottom"></div>
    <div class="regions">
      <p class="region"><span class="region-label">West Region:</span> 4172 Glen Harrow Ct, Suite #210 Englewood, Colorado 80112</p>
      <p class="region"><span class="region-label">East Region:</span> 7316 38th Ave W, Bradenton, Florida 34210</p>
    </div>
  </section>
</body>
</html>
```